Vista Chapel - Giving Hope
Sleek, Simple, Modern - Identity Package
Project: Vista Chapel - Giving Hope
Vista Chapel - Giving Hope - Religion and Spirituality
Creative Brief
Use specific fonts
open to new fonts and font changes
Simple
Ben Holloway
Chief Innovation Officer
4182 Cedar Vale Rd Atlanta, Ga 30319
404-561-3297 x 318
benh@cedarvalefold.org
www.CedarValeFold.org
Need a new fresh look for our letterhead, envelopes, labels, B. Cards etc. Also need the letterhead in Monarch size w/ matching envelopes. No deisgns that look like a law firm or accounting firm. Sleek and Modern is important.
Leave area on Back of card to make notes / write. The web address and/or some of the address info can go on the back. use our tag line someplace on the card: "Giving Hope in Christ"

```html
<!DOCTYPE html>
<html lang="en">
<head>
<meta charset="utf-8">
<title>Vista Chapel – Identity Package</title>
<link rel="stylesheet" href="https://fonts.googleapis.com/css2?family=Montserrat:wght@400;600;700&family=Open+Sans:wght@400;600&display=swap">
<style>
  :root {
    --teal: #2190b6;
    --teal-dark: #17708f;
    --ink: #1c1c1e;
    --paper: #ffffff;
    --grey-text: #6b6b6b;
    --rule: #d5d8da;
    --flap: #f4f5f6;
    --stage: #e6e7e8;
  }
  * { box-sizing: border-box; margin: 0; padding: 0; }
  html, body { width: 1200px; height: 878px; overflow: hidden; }
  body {
    background: var(--stage);
    font-family: "Open Sans", Arial, sans-serif;
    color: var(--ink);
    position: relative;
  }
  .piece {
    position: absolute;
    background: var(--paper);
    box-shadow: 0 2px 6px rgba(0,0,0,.18);
    overflow: hidden;
  }

  /* brand lockup */
  .brand { display: flex; align-items: center; gap: 6px; }
  .brand-dot { border-radius: 50%; background: var(--ink); flex: none; }
  .brand-name {
    font-family: "Montserrat", Arial, sans-serif;
    font-weight: 700;
    color: var(--ink);
    white-space: nowrap;
    letter-spacing: -.2px;
  }
  .brand--light .brand-dot { background: var(--paper); }
  .brand--light .brand-name { color: var(--paper); }
  .tagline {
    font-family: "Montserrat", Arial, sans-serif;
    font-weight: 600;
    color: var(--teal);
    letter-spacing: .3px;
    white-space: nowrap;
  }

  /* business cards */
  .card { width: 252px; height: 144px; }
  .card--teal { background: var(--teal); }
  .card--black { background: var(--ink); }
  .card-center {
    position: absolute; inset: 0;
    display: flex; flex-direction: column; align-items: center; justify-content: center; gap: 8px;
  }
  .card--teal .tagline, .card--black .tagline { color: var(--paper); font-size: 9px; }
  .card-contact { padding: 16px 18px; }
  .card-contact .brand { margin-bottom: 14px; }
  .person { font-family: "Montserrat", Arial, sans-serif; font-weight: 700; font-size: 11px; color: var(--teal); }
  .role { font-size: 8px; color: var(--grey-text); margin-bottom: 8px; }
  .contact-line { font-size: 7.5px; line-height: 1.5; color: var(--ink); }
  .card-stripe { position: absolute; left: 0; right: 0; bottom: 0; height: 6px; background: var(--teal); }
  .card-notes { padding: 16px 18px; }
  .card-notes .tagline { font-size: 9px; margin-bottom: 10px; }
  .note-line { height: 16px; border-bottom: 1px solid var(--rule); }
  .card-notes .contact-line { position: absolute; bottom: 12px; left: 18px; right: 18px; font-size: 7.5px; color: var(--grey-text); white-space: nowrap; }

  /* fax */
  .fax { width: 280px; height: 362px; padding: 22px 22px; }
  .fax-head { display: flex; justify-content: space-between; align-items: flex-start; }
  .fax-title { font-family: "Montserrat", Arial, sans-serif; font-weight: 400; font-size: 26px; letter-spacing: 3px; color: #9a9ea2; line-height: 1; }
  .fax-table { margin-top: 28px; width: 100%; border-collapse: collapse; }
  .fax-table td { font-size: 8px; padding: 5px 4px; border-bottom: 1px solid var(--rule); }
  .fax-table .label { width: 48px; font-weight: 600; color: var(--paper); background: #8d9296; }
  .fax-checks { display: grid; grid-template-columns: 1fr 1fr; gap: 8px 10px; margin-top: 20px; }
  .check { display: flex; align-items: center; gap: 5px; font-size: 8px; }
  .check-box { width: 8px; height: 8px; border: 1px solid #8d9296; }
  .sheet-foot {
    position: absolute; left: 0; right: 0; bottom: 0;
    border-top: 3px solid var(--teal);
    padding: 7px 22px 9px;
    font-size: 6.5px; line-height: 1.5; color: var(--grey-text);
  }

  /* letterhead (monarch) */
  .letterhead { width: 286px; height: 414px; padding: 26px 26px; }
  .letterhead .brand { margin-bottom: 4px; }
  .letterhead .tagline { font-size: 7px; margin-left: 30px; margin-bottom: 26px; }
  .letter-body { font-size: 7.5px; line-height: 1.55; color: #444; }
  .letter-body p { margin-bottom: 9px; }
  .signature-space { width: 90px; height: 26px; border-bottom: 1px solid #999; margin: 6px 0 5px; }
  .signer { font-weight: 600; color: var(--ink); }

  /* envelopes */
  .envelope-monarch { width: 240px; height: 124px; padding: 14px 16px; }
  .envelope-monarch .tagline { font-size: 6.5px; margin: 3px 0 5px 24px; }
  .envelope-monarch .contact-line { font-size: 6.5px; color: var(--grey-text); line-height: 1.4; }
  .envelope-monarch .card-stripe { height: 4px; }

  .envelope-back { width: 560px; height: 268px; }
  .envelope-back svg { position: absolute; inset: 0; }
  .envelope-band {
    position: absolute; left: 0; top: 0; bottom: 0; width: 150px;
    background: linear-gradient(180deg, var(--teal) 0%, var(--teal-dark) 55%, var(--ink) 100%);
  }
  .envelope-lockup {
    position: absolute; left: 150px; right: 0; top: 108px;
    display: flex; flex-direction: column; align-items: center; gap: 6px;
  }
  .envelope-lockup .tagline { font-size: 9px; padding-left: 32px; }
</style>
</head>
<body>

  <!-- Business cards -->
  <section class="piece card card--teal" style="left:40px; top:40px;">
    <div class="card-center">
      <div class="brand brand--light">
        <span class="brand-dot" style="width:26px;height:26px;"></span>
        <span class="brand-name" style="font-size:20px;">Vista Chapel</span>
      </div>
      <p class="tagline">Giving Hope in Christ</p>
    </div>
  </section>

  <section class="piece card card--black" style="left:40px; top:204px;">
    <div class="card-center">
      <div class="brand brand--light">
        <span class="brand-dot" style="width:26px;height:26px;background:var(--teal);"></span>
        <span class="brand-name" style="font-size:20px;">Vista Chapel</span>
      </div>
      <p class="tagline">Giving Hope in Christ</p>
    </div>
  </section>

  <section class="piece card card-contact" style="left:40px; top:368px;">
    <div class="brand">
      <span class="brand-dot" style="width:18px;height:18px;"></span>
      <span class="brand-name" style="font-size:13px;">Vista Chapel</span>
    </div>
    <p class="person">Ben Holloway</p>
    <p class="role">Chief Innovation Officer</p>
    <p class="contact-line">404-561-3297 x 318</p>
    <p class="contact-line">benh@cedarvalefold.org</p>
    <div class="card-stripe"></div>
  </section>

  <section class="piece card card-notes" style="left:40px; top:532px;">
    <p class="tagline">Giving Hope in Christ</p>
    <div class="note-line"></div>
    <div class="note-line"></div>
    <div class="note-line"></div>
    <p class="contact-line">4182 Cedar Vale Rd Atlanta, Ga 30319 &nbsp;·&nbsp; www.CedarValeFold.org</p>
  </section>

  <!-- Fax cover -->
  <section class="piece fax" style="left:318px; top:40px;">
    <header class="fax-head">
      <div class="brand">
        <span class="brand-dot" style="width:20px;height:20px;"></span>
        <span class="brand-name" style="font-size:14px;">Vista Chapel</span>
      </div>
      <h1 class="fax-title">FAX</h1>
    </header>
    <table class="fax-table">
      <tr><td class="label">To</td><td></td></tr>
      <tr><td class="label">From</td><td></td></tr>
      <tr><td class="label">Fax</td><td></td></tr>
      <tr><td class="label">Phone</td><td></td></tr>
      <tr><td class="label">Date</td><td></td></tr>
      <tr><td class="label">Pages</td><td></td></tr>
      <tr><td class="label">Re</td><td></td></tr>
    </table>
    <div class="fax-checks">
      <span class="check"><span class="check-box"></span>Urgent</span>
      <span class="check"><span class="check-box"></span>For Review</span>
      <span class="check"><span class="check-box"></span>Please Comment</span>
      <span class="check"><span class="check-box"></span>Please Reply</span>
    </div>
    <footer class="sheet-foot">4182 Cedar Vale Rd Atlanta, Ga 30319 · 404-561-3297 x 318<br>www.CedarValeFold.org</footer>
  </section>

  <!-- Letterhead -->
  <section class="piece letterhead" style="left:620px; top:40px;">
    <div class="brand">
      <span class="brand-dot" style="width:24px;height:24px;"></span>
      <span class="brand-name" style="font-size:17px;">Vista Chapel</span>
    </div>
    <p class="tagline">Giving Hope in Christ</p>
    <div class="letter-body">
      <p>June 12, 2024</p>
      <p>Mr. Sam Reed<br>12 Oak Street<br>Atlanta, Ga 30305</p>
      <p>Dear Friend,</p>
      <p>Thank you for your kind support of our ministry this year. Your gifts help us serve families across our city with care and hope.</p>
      <p>We look forward to sharing more news with you in the coming months as our new programs begin.</p>
      <p style="margin-bottom:0;">Sincerely,</p>
      <div class="signature-space" role="img" aria-label="Space for handwritten signature"></div>
      <p class="signer">Ben Holloway</p>
      <p>Chief Innovation Officer</p>
    </div>
    <footer class="sheet-foot">4182 Cedar Vale Rd Atlanta, Ga 30319 · 404-561-3297 x 318<br>www.CedarValeFold.org</footer>
  </section>

  <!-- Monarch envelope front -->
  <section class="piece envelope-monarch" style="left:926px; top:40px;">
    <div class="brand">
      <span class="brand-dot" style="width:18px;height:18px;"></span>
      <span class="brand-name" style="font-size:12px;">Vista Chapel</span>
    </div>
    <p class="tagline">Giving Hope in Christ</p>
    <p class="contact-line">4182 Cedar Vale Rd<br>Atlanta, Ga 30319</p>
    <div class="card-stripe"></div>
  </section>

  <!-- Small cards column -->
  <section class="piece card card--black" style="left:926px; top:184px; width:240px; height:137px;">
    <div class="card-center">
      <div class="brand brand--light">
        <span class="brand-dot" style="width:22px;height:22px;background:var(--teal);"></span>
        <span class="brand-name" style="font-size:17px;">Vista Chapel</span>
      </div>
      <p class="tagline">Giving Hope in Christ</p>
    </div>
  </section>

  <section class="piece card card-contact" style="left:926px; top:341px; width:240px; height:137px;">
    <div class="brand">
      <span class="brand-dot" style="width:16px;height:16px;"></span>
      <span class="brand-name" style="font-size:12px;">Vista Chapel</span>
    </div>
    <p class="person">Ben Holloway</p>
    <p class="role">Chief Innovation Officer</p>
    <p class="contact-line">benholl58</p>
    <p class="contact-line">www.CedarValeFold.org</p>
    <div class="card-stripe"></div>
  </section>

  <!-- DL envelope back -->
  <section class="piece envelope-back" style="left:318px; top:486px;">
    <svg width="560" height="268" viewBox="0 0 560 268" aria-hidden="true">
      <path d="M150 0 H560 L370 150 Q355 160 340 150 Z" fill="var(--flap)" stroke="var(--rule)"/>
    </svg>
    <div class="envelope-band" role="img" aria-label="Decorative brand colour area in teal and black"></div>
    <div class="envelope-lockup">
      <div class="brand">
        <span class="brand-dot" style="width:26px;height:26px;"></span>
        <span class="brand-name" style="font-size:20px;">Vista Chapel</span>
      </div>
      <p class="tagline">Giving Hope in Christ</p>
    </div>
  </section>

</body>
</html>
```